Risk Management Company in need of Business Card Design

We sell risk management insurance to Lenders (Banks, Credit Unions, Real Estate Trust).

We need a very clean, professional card that will leave a great impression.

We are looking to use a blue color for our logo on the card (Preferably close to royal blue but are open to looking at navy blue or any darker blues as well).

Please see the logo attached to get an idea. We are open to writing Harbor Vault Under the logo or next to the logo. Really whatever looks best.

Target Market(s)

Banks, Credit Unions, Real Estate Trusts

Industry/Entity Type

Insurance

Contact Information for Business Card

Name: Mark Dunstan
Title: Regional Sales Director
Email: mdunstan@harborvault-example.net
C:555-318-2047
D:555-674-1192
800-555-0147 Ext.312
F:555-829-6630 (We would like to see some cards without the fax number as well to compare)

Company Name: Harbor Vault
Website: www.harborvault-example.net

Address: 418 E. Marlowe St. Suite 140, Elmridge, PA 19099 (Preferably written on the bottom of the card in small print.)

Colors
0355a3
0455a3

Requirements
Nice to have
• We would like to see a couple of where the back has the logo in reverse colors (Logo White, Background Blue)

```html
<!DOCTYPE html>
<html lang="en">
<head>
<meta charset="utf-8">
<title>Harbor Vault — Business Cards</title>
<link rel="stylesheet" href="https://fonts.googleapis.com/css2?family=Cinzel:wght@600&family=Roboto+Condensed:ital,wght@0,400;1,700&display=swap">
<style>
  :root {
    --navy: #101a66;
    --white: #ffffff;
    --backdrop: #e7e8ec;
    --shadow: rgba(16, 26, 102, 0.18);
  }
  * { box-sizing: border-box; margin: 0; padding: 0; }
  html, body { width: 1200px; height: 900px; overflow: hidden; }
  body {
    background: var(--backdrop);
    position: relative;
    font-family: "Roboto Condensed", "Arial Narrow", sans-serif;
  }
  .card {
    position: absolute;
    width: 540px;
    height: 309px;
    box-shadow: 0 10px 28px var(--shadow);
    overflow: hidden;
  }
  .card-front { left: 330px; top: 50px; background: var(--navy); }
  .card-back { top: 450px; background: var(--white); }
  .card-back.no-fax { left: 40px; }
  .card-back.with-fax { left: 620px; }

  .stripes { position: absolute; inset: 0; }

  .brand {
    position: absolute;
    display: flex;
    align-items: center;
    gap: 10px;
    font-family: "Cinzel", "Times New Roman", serif;
    font-weight: 600;
    letter-spacing: 1px;
    white-space: nowrap;
  }
  .brand-mark { display: block; }
  .card-front .brand {
    left: 36px; top: 150px;
    color: var(--white);
    font-size: 30px;
  }
  .card-front .brand-mark { width: 22px; height: 22px; background: var(--white); }
  .card-back .brand {
    right: 26px; top: 30px;
    color: var(--navy);
    font-size: 19px;
  }
  .card-back .brand-mark { width: 14px; height: 14px; background: var(--navy); }

  .website {
    position: absolute;
    right: 34px; bottom: 40px;
    color: var(--white);
    font-size: 15px;
    letter-spacing: 0.3px;
  }

  .name-tab {
    position: absolute;
    left: 0; top: 26px;
    width: 215px; height: 44px;
    background: var(--navy);
    color: var(--white);
    padding: 3px 0 0 40px;
  }
  .person-name {
    font-style: italic;
    font-weight: 700;
    font-size: 19px;
    line-height: 22px;
    text-transform: uppercase;
  }
  .person-title { font-size: 11px; line-height: 14px; }

  .contact-list {
    position: absolute;
    right: 22px;
    list-style: none;
  }
  .no-fax .contact-list { bottom: 26px; }
  .with-fax .contact-list { bottom: 22px; }
  .contact-row {
    display: flex;
    align-items: center;
    gap: 8px;
    margin-top: 5px;
  }
  .contact-icon { width: 14px; height: 14px; fill: var(--navy); flex: none; }
  .contact-bar {
    width: 235px;
    height: 18px;
    background: var(--navy);
    color: var(--white);
    font-size: 11px;
    line-height: 18px;
    padding-left: 8px;
    white-space: nowrap;
    overflow: hidden;
  }
</style>
</head>
<body>

<svg width="0" height="0" style="position:absolute" aria-hidden="true">
  <defs>
    <symbol id="icon-phone" viewBox="0 0 16 16"><path d="M1 5c0-2 3-3 7-3s7 1 7 3v1h-4V5H5v1H1zM3 8h10l1 6H2z"/></symbol>
    <symbol id="icon-mail" viewBox="0 0 16 16"><path d="M1 3h14v10H1zM2 4.5v.3l6 4 6-4v-.3z" fill-rule="evenodd"/></symbol>
    <symbol id="icon-mobile" viewBox="0 0 16 16"><path d="M4 1h8v14H4zM5.5 3v9h5V3z" fill-rule="evenodd"/></symbol>
    <symbol id="icon-fax" viewBox="0 0 16 16"><path d="M4 1h8v4H4zM1 6h14v6h-3v3H4v-3H1zM5 10v3h6v-3z" fill-rule="evenodd"/></symbol>
    <symbol id="icon-home" viewBox="0 0 16 16"><path d="M8 1l7 7h-2v7H9v-4H7v4H3V8H1z"/></symbol>
  </defs>
</svg>

<section class="card card-front" aria-label="Card front">
  <svg class="stripes" viewBox="0 0 540 309" aria-hidden="true">
    <polygon points="230,48 540,22 540,30 232,56" fill="#ffffff"/>
    <polygon points="0,270 290,242 292,252 0,282" fill="#ffffff"/>
  </svg>
  <div class="brand"><span class="brand-mark"></span>Harbor Vault</div>
  <p class="website">www.harborvault-example.net</p>
</section>

<section class="card card-back no-fax" aria-label="Card back without fax">
  <div class="name-tab">
    <p class="person-name">Mark Dunstan</p>
    <p class="person-title">Regional Sales Director</p>
  </div>
  <div class="brand"><span class="brand-mark"></span>Harbor Vault</div>
  <ul class="contact-list">
    <li class="contact-row"><svg class="contact-icon"><use href="#icon-phone"/></svg><span class="contact-bar">555-674-1192 / 800-555-0147 Ext.312</span></li>
    <li class="contact-row"><svg class="contact-icon"><use href="#icon-mail"/></svg><span class="contact-bar">mdunstan@harborvault-example.net</span></li>
    <li class="contact-row"><svg class="contact-icon"><use href="#icon-mobile"/></svg><span class="contact-bar">555-318-2047</span></li>
    <li class="contact-row"><svg class="contact-icon"><use href="#icon-home"/></svg><span class="contact-bar">418 E. Marlowe St. Suite 140, Elmridge, PA 19099</span></li>
  </ul>
</section>

<section class="card card-back with-fax" aria-label="Card back with fax">
  <div class="name-tab">
    <p class="person-name">Mark Dunstan</p>
    <p class="person-title">Regional Sales Director</p>
  </div>
  <div class="brand"><span class="brand-mark"></span>Harbor Vault</div>
  <ul class="contact-list">
    <li class="contact-row"><svg class="contact-icon"><use href="#icon-phone"/></svg><span class="contact-bar">555-674-1192 / 800-555-0147 Ext.312</span></li>
    <li class="contact-row"><svg class="contact-icon"><use href="#icon-mail"/></svg><span class="contact-bar">mdunstan@harborvault-example.net</span></li>
    <li class="contact-row"><svg class="contact-icon"><use href="#icon-mobile"/></svg><span class="contact-bar">555-318-2047</span></li>
    <li class="contact-row"><svg class="contact-icon"><use href="#icon-fax"/></svg><span class="contact-bar">555-829-6630</span></li>
    <li class="contact-row"><svg class="contact-icon"><use href="#icon-home"/></svg><span class="contact-bar">418 E. Marlowe St. Suite 140, Elmridge, PA 19099</span></li>
  </ul>
</section>

</body>
</html>
```